Business Card Project

We are a small consulting firm. You can experiment with any design.
Must have:
1) Company name - OLUNDEX International
2) Company slogan - simple solutions for complex problems
3) Name/Title/Phone/Email/WWW/ - use anything you like as an example.

Industry/Entity Type

Business

```html
<!DOCTYPE html>
<html lang="en">
<head>
<meta charset="utf-8">
<title>OLUNDEX International – Business Card</title>
<link rel="stylesheet" href="https://fonts.googleapis.com/css2?family=Arimo:wght@400;700&display=swap">
<style>
  :root {
    --backdrop: #e9e7e4;
    --card: #ffffff;
    --brand-blue: #1a87d0;
    --brand-grey: #5b5d60;
    --ink: #141414;
    --soft-grey: #6d6f72;
    --card-shadow: rgba(0, 0, 0, 0.18);
  }
  * { box-sizing: border-box; margin: 0; padding: 0; }
  html, body {
    width: 1200px;
    height: 983px;
    overflow: hidden;
    background: var(--backdrop);
    font-family: "Arimo", Arial, sans-serif;
  }
  .sheet {
    position: relative;
    width: 1200px;
    height: 983px;
  }
  .card {
    position: absolute;
    left: 215px;
    width: 770px;
    height: 440px;
    background: var(--card);
    box-shadow: 0 6px 24px var(--card-shadow);
    overflow: hidden;
  }
  .card--back { top: 34px; }
  .card--front { top: 509px; }

  /* Wordmark */
  .wordmark {
    display: flex;
    align-items: center;
    gap: 16px;
  }
  .wordmark__dot {
    width: 44px;
    height: 44px;
    border-radius: 50%;
    background: var(--brand-blue);
    flex: none;
  }
  .wordmark__name {
    color: var(--brand-grey);
    font-weight: 400;
    font-size: 40px;
    letter-spacing: 2px;
    line-height: 1;
    white-space: nowrap;
  }

  /* Back side */
  .card--back .wordmark {
    position: absolute;
    left: 0;
    right: 0;
    top: 170px;
    justify-content: center;
  }
  .card--back .website {
    position: absolute;
    left: 0;
    right: 0;
    top: 290px;
    text-align: center;
    color: var(--brand-blue);
    font-size: 22px;
  }

  /* Front side */
  .card--front .brand-block {
    position: absolute;
    left: 46px;
    top: 110px;
  }
  .card--front .wordmark__name { font-size: 30px; letter-spacing: 1.5px; }
  .card--front .wordmark__dot { width: 36px; height: 36px; }
  .slogan {
    margin-top: 10px;
    color: var(--brand-blue);
    font-size: 15px;
  }
  .fold-panel {
    position: absolute;
    left: 400px;
    top: 0;
    width: 370px;
    height: 440px;
    background: linear-gradient(90deg, #d9d9d9 0%, #f4f4f4 18%, #ffffff 40%);
  }
  .person {
    position: absolute;
    left: 450px;
    top: 150px;
  }
  .person__name {
    color: var(--brand-blue);
    font-size: 30px;
    letter-spacing: 0.5px;
  }
  .person__title {
    color: var(--soft-grey);
    font-size: 18px;
    margin-top: 2px;
  }
  .person__phone {
    color: var(--ink);
    font-size: 25px;
    margin-top: 16px;
    letter-spacing: 0.5px;
  }
  .contact-lines {
    position: absolute;
    left: 150px;
    top: 310px;
    color: var(--soft-grey);
    font-size: 22px;
    line-height: 1.3;
  }
</style>
</head>
<body>
  <main class="sheet">
    <section class="card card--back" aria-label="Business card, back side">
      <div class="wordmark">
        <span class="wordmark__dot"></span>
        <span class="wordmark__name">OLUNDEX International</span>
      </div>
      <p class="website">www.olundexinternational.com</p>
    </section>

    <section class="card card--front" aria-label="Business card, front side">
      <div class="fold-panel"></div>
      <div class="brand-block">
        <div class="wordmark">
          <span class="wordmark__dot"></span>
          <span class="wordmark__name">OLUNDEX International</span>
        </div>
        <p class="slogan">simple solutions for complex problems</p>
      </div>
      <div class="person">
        <p class="person__name">YOUR NAME</p>
        <p class="person__title">CEO, Founder</p>
        <p class="person__phone">T: +91 8000 555 014</p>
      </div>
      <div class="contact-lines">
        <p class="contact-lines__email">info@olundexinternational.com</p>
        <p class="contact-lines__web">www.olundexinternational.com</p>
      </div>
    </section>
  </main>
</body>
</html>
```